BriarCove Anesthesia Solutions, PC

I need a business card /logo for my new business. I would like it to have some type of ? EKG or medical symbol built into the name( I am on the North side of Lake Pellridge where mountains and water are visible.
I would like this saying on the front," Calm Hands, Steady Care"
My company provides anesthesia services to outparient endoscopy units, eye centers, pain & podiatry offices.

Target Market(s)

Gastroenterologists, podiatrists, eye doctors, pain doctors

Industry/Entity Type

Medical

Contact Information for Business Card

I would like to incorporate a medical symbol(EKG, stethoscope, etc) into the name or scenery if possible

Colors
3377b5
add136
fbee3d

Requirements
Must have
• Business name( BriarCove Sedation Care, PC).....
• "Calm Hands, Steady Care",
• my email: briarcoveanesthesiacare.example,
• 555-214-9087
Nice to have
• Incorporate water &/or mountains

```html
<!DOCTYPE html>
<html lang="en">
<head>
<meta charset="utf-8">
<title>BriarCove Sedation Care, PC — Business Card</title>
<link rel="stylesheet" href="https://fonts.googleapis.com/css2?family=Arimo:wght@400;700&family=Great+Vibes&display=swap">
<style>
  :root {
    --brand-blue: #1f66a6;
    --brand-green: #9dc13a;
    --ink: #2b2b2b;
    --card-light: #f4f4f6;
    --card-mid: #d9dbe2;
    --lake-top: #a9abb9;
    --lake-mid: #c6c8d2;
    --lake-low: #b9bac6;
    --backdrop: #ece9e4;
  }
  html, body {
    margin: 0;
    padding: 0;
    width: 1200px;
    height: 800px;
    overflow: hidden;
    background: var(--backdrop);
  }
  .canvas {
    position: relative;
    width: 1200px;
    height: 800px;
    font-family: "Arimo", Arial, sans-serif;
  }
  .card {
    position: absolute;
    width: 520px;
    height: 290px;
    border-radius: 12px;
    overflow: hidden;
    box-shadow: 0 6px 18px rgba(0,0,0,0.18);
  }
  .card--front { left: 336px; top: 80px; }
  .card--back {
    left: 326px;
    top: 400px;
    background: radial-gradient(ellipse at 40% 45%, var(--card-light) 0%, var(--card-mid) 100%);
  }
  .scenery {
    position: absolute;
    inset: 0;
    background: linear-gradient(180deg, var(--lake-top) 0%, #b3b4c1 14%, var(--lake-mid) 30%, #d0d1da 60%, var(--lake-low) 100%);
  }
  .wordmark {
    position: absolute;
    line-height: 1;
  }
  .wordmark__name {
    display: block;
    color: var(--brand-blue);
    font-weight: 700;
    letter-spacing: -1px;
  }
  .wordmark__descriptor {
    display: block;
    color: var(--ink);
    font-weight: 400;
  }
  .card--front .wordmark {
    left: 0; right: 0;
    top: 92px;
    text-align: center;
  }
  .card--front .wordmark__name { font-size: 54px; }
  .card--front .wordmark__descriptor { font-size: 19px; margin-top: 10px; }
  .tagline {
    position: absolute;
    left: 0; right: 0;
    top: 212px;
    margin: 0;
    text-align: center;
    font-family: "Great Vibes", cursive;
    font-size: 24px;
    color: var(--ink);
  }
  .card--back .wordmark {
    left: 58px;
    top: 40px;
  }
  .card--back .wordmark__name { font-size: 48px; }
  .card--back .wordmark__descriptor { font-size: 17px; margin-top: 10px; margin-left: 62px; }
  .person {
    position: absolute;
    left: 60px;
    top: 152px;
    font-size: 20px;
    font-weight: 700;
    color: var(--brand-blue);
  }
  .person__surname { color: var(--brand-green); font-weight: 400; }
  .contact {
    position: absolute;
    left: 56px;
    top: 195px;
    margin: 0;
    padding: 0;
    list-style: none;
    font-size: 12.5px;
    line-height: 16px;
    color: var(--ink);
  }
  .contact__label { color: var(--brand-blue); }
</style>
</head>
<body>
<main class="canvas">
  <section class="card card--front" aria-label="Card front">
    <div class="scenery" role="img" aria-label="Photograph of a wooden dock reaching into a calm misty lake with a wooded shoreline under a grey sky"></div>
    <div class="wordmark">
      <span class="wordmark__name">BriarCove</span>
      <span class="wordmark__descriptor">Sedation Care, PC</span>
    </div>
    <p class="tagline">“Calm Hands, Steady Care”</p>
  </section>

  <section class="card card--back" aria-label="Card back">
    <div class="wordmark">
      <span class="wordmark__name">BriarCove</span>
      <span class="wordmark__descriptor">Sedation Care, PC</span>
    </div>
    <div class="person">Dana <span class="person__surname">Wells</span></div>
    <ul class="contact">
      <li><span class="contact__label">p :</span> 555-214-9087</li>
      <li><span class="contact__label">e :</span> dana@briarcoveanesthesiacare.example</li>
      <li>www.briarcoveanesthesiacare.example</li>
    </ul>
  </section>
</main>
</body>
</html>
```